StageLoop - Music Industry App needs a top quality wordpress homepage

We need a modern responsive wordpress homepage built. Our website will only feature one page with the goal to get people to sign up to our app. A word document has been uploaded outlining the page content/sections.

Once the homepage is finalised, I will also need 2 landing pages built as part of this competition. It will be very similar to the homepage with the same layout etc but just feature different images and content. The homepage is for anyone (artists and venues) to find out about us but the landing pages will be artist or venue specific.

The completed work must be delivered as an exportable file into wordpress and be designed properly so no more work is needed to begin utilising as the actual website. The images used must be setup correctly for speed and quality also.

Target Market(s)

Venues and Artists.

Coding

Coded - Design and coding required

Requirements
Must have
• UPDATE: High Res Logo files attached
• Must be a modern looking website and be responsive. Must look good across all devices from desktop, to mobile and tablet. Needs to be very high quality.
• Please see the attached logo - I am waiting for the final high quality version and will reupload when complete but this will be enough to get you started for now. The website must have a dark base colour and have red/white elements to match the logo. The red colour used MUST match the red colour used in the logo.
• Please have a go at creating it how you think is best and provide feedback from there. I am leaving it very open to the designers so I can get the best website possible and lots of different ideas etc.

```html
<!DOCTYPE html>
<html lang="en">
<head>
<meta charset="utf-8">
<title>StageLoop – Live Music Booking</title>
<link href="https://fonts.googleapis.com/css2?family=Montserrat:wght@400;600;700&family=Roboto:wght@300;400;500;700&display=swap" rel="stylesheet">
<style>
:root{
  --red:#e1141c;
  --red-soft:#fbe3e4;
  --ink:#1d1d1f;
  --text:#3a3a3a;
  --muted:#8a8a8a;
  --pale:#edf1f9;
  --frame:#b3b3b3;
  --footer:#2a2a2a;
  --white:#fff;
}
*{box-sizing:border-box;margin:0;padding:0}
html,body{width:1200px;height:2662px;overflow:hidden}
body{background:var(--frame);font-family:'Roboto',sans-serif;color:var(--text);position:relative}
.page{position:absolute;left:234px;top:0;width:732px;height:2662px;background:var(--white)}
.section{position:absolute;left:0;width:732px}
.abs{position:absolute;z-index:2}
.h2{font-family:'Montserrat',sans-serif;font-weight:600;font-size:17px;color:var(--ink);text-align:center;width:100%;left:0}
.decor{position:absolute;background:var(--red-soft);opacity:.7;z-index:1}
.tick{width:11px;height:11px;flex:none}
.btn-red{background:var(--red);color:var(--white);border:none;border-radius:4px;font-weight:700;display:flex;align-items:center;justify-content:center;font-family:'Roboto',sans-serif}

/* nav */
.nav{top:0;height:45px;background:var(--white)}
.brand{left:143px;top:0;width:53px;height:45px;background:#000;display:flex;flex-direction:column;align-items:center;justify-content:center;gap:3px}
.brand .dot{width:12px;height:12px;border-radius:50%;background:var(--red)}
.brand span{font-size:8px;color:var(--white);font-weight:500}
.nav-link{top:18px;font-size:7px;color:var(--ink)}
.nav-sign{color:var(--red)}
.nav-login{left:534px;top:12px;width:56px;height:21px;border:1px solid var(--red);border-radius:5px;font-size:7px;color:var(--red);display:flex;align-items:center;justify-content:center}

/* hero */
.hero{top:45px;height:368px}
.hero-bg{position:absolute;inset:0;background:radial-gradient(ellipse at 75% 30%,#d9a43a 0%,#d1601f 30%,#8a1d12 60%,#1b0a08 100%)}
.hero-shade{position:absolute;inset:0;background:linear-gradient(90deg,rgba(10,5,5,.75) 0%,rgba(10,5,5,.35) 55%,rgba(0,0,0,0) 100%)}
.hero h1{left:143px;top:68px;font-family:'Roboto',sans-serif;font-weight:700;font-size:22px;color:var(--white)}
.hero-sub{left:143px;top:105px;width:220px;font-size:11.5px;line-height:18px;color:var(--white)}
.field{left:143px;width:218px;height:28px;border-radius:4px;background:rgba(255,255,255,.45);color:var(--white);font-size:8px;font-weight:700;padding-left:7px;display:flex;align-items:center}
.hero-terms{left:143px;top:236px;font-size:5.8px;color:var(--white)}
.hero-terms u{text-decoration:underline}
.hero-cta{left:143px;top:252px;width:218px;height:27px;font-size:8px}
.phone{background:#0d0d0f;border:3px solid #222;border-radius:16px;overflow:hidden}
.phone-art{position:absolute;left:7px;top:18px;right:7px;height:140px;border-radius:4px;background:linear-gradient(160deg,#1f2a68 0%,#5b1d4a 50%,#b0182a 100%)}
.phone-art-title{position:absolute;left:12px;top:108px;font-family:'Montserrat',sans-serif;font-size:7.5px;font-weight:600;color:var(--white);line-height:10px;width:70px}
.phone-play{position:absolute;left:12px;top:138px;width:42px;height:10px;background:var(--red);border-radius:2px;font-size:4px;color:#fff;display:flex;align-items:center;padding-left:8px}
.phone-row{position:absolute;left:12px;right:12px;height:1px;background:#2b2b2e}
.phone-row::before{content:"";position:absolute;left:20px;top:-5px;width:40px;height:3px;background:#8a8a8a;border-radius:2px}

/* how */
.how{top:413px;height:366px;background:var(--white)}
.how-phone{left:143px;top:91px;width:102px;height:209px}
.steps{left:301px;top:148px;list-style:none}
.steps li{display:flex;align-items:center;gap:11px;font-size:8px;height:23px;color:var(--text)}

/* why */
.why{top:779px;height:366px;background:var(--pale)}
.card{top:86px;width:103px;height:184px;background:var(--white);box-shadow:0 8px 10px -4px rgba(225,20,28,.35);text-align:center}
.card-icon{position:absolute;left:30px;top:16px;width:44px;height:44px}
.card h3{position:absolute;left:0;right:0;top:78px;font-family:'Montserrat',sans-serif;font-size:11.5px;color:var(--red);font-weight:600}
.card p{position:absolute;left:10px;right:10px;top:104px;font-size:6.8px;line-height:13.5px;color:var(--muted)}

/* venues / artists */
.match{top:1145px;height:367px;background:var(--white)}
.col-title{top:52px;font-family:'Montserrat',sans-serif;font-weight:600;font-size:17px;color:var(--ink);width:218px;text-align:center}
.bullets{top:85px;width:225px;list-style:none}
.bullets li{display:flex;align-items:center;gap:10px;height:23px;font-size:5.8px;color:var(--ink);letter-spacing:-.1px}
.note{top:212px;width:220px;font-size:5.8px;line-height:15.5px;color:var(--ink)}
.note-small{top:266px;font-size:5px;color:var(--muted)}
.note-small b{color:var(--red);font-weight:400}
.signup{top:285px;width:218px;height:28px;border:1px solid #f2a9ac;border-radius:5px;background:var(--white)}
.signup span{position:absolute;left:6px;top:9px;font-size:7.5px;color:#c0c0c0}
.signup .btn-red{position:absolute;right:2px;top:2px;width:82px;height:22px;font-size:8px;font-weight:500}

/* download */
.download{top:1512px;height:243px;background:var(--pale)}
.dl-text{left:211px;top:98px;width:310px;text-align:center;font-size:6.2px;line-height:12.5px;color:var(--ink)}
.store{top:160px;width:122px;height:25px;font-size:7px;font-weight:700;display:flex;align-items:center;gap:10px;padding-left:12px}
.store i{width:11px;height:11px;border-radius:50%;display:block}
.store-a{left:227px;background:var(--red);color:var(--white)}
.store-a i{background:var(--white)}
.store-b{left:362px;background:var(--white);border:1px solid var(--red);color:var(--red)}
.store-b i{background:var(--red)}

/* team */
.team{top:1755px;height:313px;background:var(--white)}
.team-sub{top:92px;left:0;width:100%;text-align:center;font-size:8px;color:var(--muted)}
.member{top:115px;width:141px;height:149px;background:var(--red);padding:4px}
.member-photo{width:133px;height:121px}
.member-name{position:absolute;left:7px;top:127px;font-size:6px;font-weight:700;color:var(--white);line-height:9px}
.member-name small{display:block;font-weight:400}
.socials{position:absolute;right:6px;top:130px;display:flex;gap:5px}
.socials i{width:6px;height:6px;border-radius:50%;background:var(--white);display:block}

/* contact */
.contact{top:2068px;height:358px;background:var(--pale)}
.contact-sub{top:92px;left:0;width:100%;text-align:center;font-size:8.5px;color:var(--ink)}
.input{left:205px;width:323px;background:var(--white);font-size:6.5px;color:var(--muted);padding:8px 10px}
.send{left:331px;top:283px;width:70px;height:19px;font-size:8px;font-weight:500;border-radius:2px}

/* footer */
.footer{top:2426px;height:236px;background:var(--footer);color:var(--white)}
.f-brand{left:33px;top:50px;display:flex;flex-direction:column;align-items:center;gap:3px}
.f-brand .dot{width:14px;height:14px;border-radius:50%;background:var(--red)}
.f-brand span{font-size:9px}
.f-about{left:35px;top:97px;width:112px;font-size:8.6px;line-height:12.3px}
.f-col{top:54px}
.f-col h4{font-family:'Montserrat',sans-serif;font-size:12px;font-weight:600;margin-bottom:10px}
.f-col li{list-style:none;font-size:8.3px;line-height:17px}
.f-news h4{font-weight:400}
.news{left:578px;top:88px;width:131px;height:17px;display:flex}
.news span{flex:1;background:var(--white);font-size:5px;color:var(--muted);padding:6px 5px 0}
.news b{width:45px;background:var(--red);font-size:7px;display:flex;align-items:center;justify-content:center}
.f-rule{left:35px;top:190px;width:674px;height:1px;background:#4a4a4a}
.f-copy{left:35px;top:210px;font-size:8px}
.f-legal{right:23px;top:210px;font-size:8px;display:flex;gap:9px}
</style>
</head>
<body>
<svg width="0" height="0" style="position:absolute">
  <defs>
    <symbol id="tick" viewBox="0 0 12 12"><circle cx="6" cy="6" r="6" fill="#e1141c"/><path d="M3.3 6.2l1.8 1.8 3.6-3.7" fill="none" stroke="#fff" stroke-width="1.4" stroke-linecap="round" stroke-linejoin="round"/></symbol>
    <symbol id="badge" viewBox="0 0 44 44"><circle cx="22" cy="22" r="21" fill="#fbd4d6"/><circle cx="22" cy="22" r="17" fill="#e1141c"/></symbol>
  </defs>
</svg>

<main class="page">
  <div class="decor" style="left:564px;top:413px;width:168px;height:116px"></div>
  <div class="decor" style="left:0;top:662px;width:121px;height:117px"></div>
  <div class="decor" style="left:564px;top:1145px;width:168px;height:117px"></div>
  <div class="decor" style="left:0;top:1395px;width:121px;height:117px"></div>
  <div class="decor" style="left:564px;top:1728px;width:168px;height:117px"></div>
  <div class="decor" style="left:0;top:1978px;width:121px;height:117px"></div>

  <header class="section nav">
    <div class="abs brand"><i class="dot"></i><span>StageLoop</span></div>
    <a class="abs nav-link" style="left:256px">Home</a>
    <a class="abs nav-link" style="left:306px">Our Works</a>
    <a class="abs nav-link" style="left:369px">Why Us</a>
    <a class="abs nav-link" style="left:421px">About</a>
    <a class="abs nav-link nav-sign" style="left:488px">Sign up</a>
    <span class="abs nav-link" style="left:519px">or</span>
    <a class="abs nav-login">Log in</a>
  </header>

  <section class="section hero">
    <div class="hero-bg" role="img" aria-label="Concert crowd with raised hands under warm orange stage lights"></div>
    <div class="hero-shade"></div>
    <h1 class="abs">Rydo for Live Music</h1>
    <p class="abs hero-sub">StageLoop connects venues with artists to make booking gigs simple</p>
    <div class="abs field" style="top:158px">Email</div>
    <div class="abs field" style="top:198px">Password</div>
    <p class="abs hero-terms">By clicking Sign up, I agree to the <u>Terms of Conditions</u> &amp; <u>Privacy Policy</u></p>
    <button class="abs btn-red hero-cta">SIGN UP FOR FREE</button>
    <div class="abs phone" style="left:464px;top:54px;width:125px;height:260px">
      <div class="phone-art" role="img" aria-label="Featured album artwork of a singer in blue and red light"></div>
      <div class="phone-art-title">New Album from Nova Reyes</div>
      <div class="phone-play">PLAY</div>
      <div class="phone-row" style="top:190px"></div>
      <div class="phone-row" style="top:206px"></div>
      <div class="phone-row" style="top:222px"></div>
      <div class="phone-row" style="top:238px"></div>
    </div>
  </section>

  <section class="section how">
    <h2 class="abs h2" style="top:55px">How StageLoop Works</h2>
    <div class="abs phone how-phone">
      <div class="phone-row" style="top:30px"></div>
      <div class="phone-row" style="top:43px"></div>
      <div class="phone-row" style="top:56px"></div>
      <div class="phone-row" style="top:69px"></div>
      <div class="phone-row" style="top:82px"></div>
      <div style="position:absolute;left:10px;right:10px;top:113px;height:8px;background:var(--red);border-radius:2px"></div>
      <div style="position:absolute;left:8px;right:8px;top:143px;height:50px;border-radius:3px;background:linear-gradient(120deg,#3a1f6a,#b3183a 50%,#1c3e6e)" role="img" aria-label="Recommended album artwork"></div>
    </div>
    <ul class="abs steps">
      <li><svg class="tick"><use href="#tick"/></svg>Artists and venues sign up for free and create a profile</li>
      <li><svg class="tick"><use href="#tick"/></svg>Venues search for an artist for their upcoming gigs</li>
      <li><svg class="tick"><use href="#tick"/></svg>Venues request a quote and communicate with the artist direct</li>
      <li><svg class="tick"><use href="#tick"/></svg>The gig is booked in once payment is provided by the venue.</li>
      <li><svg class="tick"><use href="#tick"/></svg>Upon completion the money is paid to the artist within 48 hours or less.</li>
    </ul>
  </section>

  <section class="section why">
    <h2 class="abs h2" style="top:52px">Why StageLoop</h2>
    <article class="abs card" style="left:143px">
      <svg class="card-icon" viewBox="0 0 44 44"><use href="#badge"/><path d="M22 30s-8-5-8-10a4.2 4.2 0 0 1 8-2 4.2 4.2 0 0 1 8 2c0 5-8 10-8 10z" fill="none" stroke="#fff" stroke-width="1.6"/></svg>
      <h3>Simple</h3><p>StageLoop makes gig booking easy for both the venue and artist.</p>
    </article>
    <article class="abs card" style="left:258px">
      <svg class="card-icon" viewBox="0 0 44 44"><use href="#badge"/><g fill="none" stroke="#fff" stroke-width="1.6"><rect x="13" y="19" width="11" height="6" rx="3" transform="rotate(-45 18.5 22)"/><rect x="20" y="19" width="11" height="6" rx="3" transform="rotate(-45 25.5 22)"/></g></svg>
      <h3>Connect</h3><p>Join the StageLoop community which is full of amazing artists and venues.</p>
    </article>
    <article class="abs card" style="left:372px">
      <svg class="card-icon" viewBox="0 0 44 44"><use href="#badge"/><path d="M22 12l8 3v6c0 5-4 9-8 11-4-2-8-6-8-11v-6z" fill="none" stroke="#fff" stroke-width="1.6"/><path d="M18.5 22l2.5 2.5 4.5-5" fill="none" stroke="#fff" stroke-width="1.6"/></svg>
      <h3>Protection</h3><p>StageLoop makes gig booking easy for both the venue and artist.</p>
    </article>
    <article class="abs card" style="left:487px">
      <svg class="card-icon" viewBox="0 0 44 44"><use href="#badge"/><circle cx="22" cy="22" r="10" fill="none" stroke="#fff" stroke-width="1.6"/><text x="22" y="26.5" text-anchor="middle" font-family="Roboto,sans-serif" font-size="12" fill="#fff">$</text></svg>
      <h3>Price</h3><p>StageLoop makes gig booking easy for both the venue and artist.</p>
    </article>
  </section>

  <section class="section match">
    <h2 class="abs col-title" style="left:143px">Venues</h2>
    <h2 class="abs col-title" style="left:372px">Artists</h2>
    <ul class="abs bullets" style="left:143px">
      <li><svg class="tick"><use href="#tick"/></svg>StageLoop is a 100% FREE service for all venues - you pay us nothing!</li>
      <li><svg class="tick"><use href="#tick"/></svg>Get instant access to hundreds of artists around your local community</li>
      <li><svg class="tick"><use href="#tick"/></svg>All genres to suit any venue from a pub to a wedding or even a nightclub</li>
      <li><svg class="tick"><use href="#tick"/></svg>Simple booking process with a money back guarantee</li>
      <li><svg class="tick"><use href="#tick"/></svg>Communicate directly with the artist and negotiate the price</li>
    </ul>
    <ul class="abs bullets" style="left:372px;width:240px">
      <li><svg class="tick"><use href="#tick"/></svg>Sign up to StageLoop for FREE and get yourself in front of venues</li>
      <li><svg class="tick"><use href="#tick"/></svg>Only pay us if you get a gig - we only get 5% of the fee you charge the venue</li>
      <li><svg class="tick"><use href="#tick"/></svg>All genres and artists welcome - as long as you're experienced and professional</li>
      <li><svg class="tick"><use href="#tick"/></svg>Get paid within 48 hours or less after the gig guaranteed!</li>
      <li><svg class="tick"><use href="#tick"/></svg>Negotiate your price and don't pay huge agent fees to ensure you earn top</li>
    </ul>
    <p class="abs note" style="left:143px">StageLoop is not yet ready to host gigs as we're currently working on building our artists. We are launching for venues in Q4 2019. Pre-register now to keep informed and be one of the first people to use our platform.</p>
    <p class="abs note" style="left:372px">StageLoop is not yet ready to host gigs as we're currently working on building our artists. We are launching for venues in Q4 2019. Pre-register now to keep informed and be one of the first people to use our platform.</p>
    <p class="abs note note-small" style="left:372px"><b>*Sign up</b> and <u>create</u> your StageLoop profile now</p>
    <div class="abs signup" style="left:143px"><span>Enter your E-mail</span><button class="btn-red">Pre Register</button></div>
    <div class="abs signup" style="left:372px"><span>Enter your E-mail</span><button class="btn-red">Register</button></div>
  </section>

  <section class="section download">
    <h2 class="abs h2" style="top:55px">Download App</h2>
    <p class="abs dl-text">Everything about Loopster is designed to be easy. You can download it right now from the App Shelf or Play Shelf. Moreover, with just a few steps, you can migrate your content automatically and securely from your older device with the Move to Phone app.</p>
    <a class="abs store store-a"><i></i>Available on App Shelf</a>
    <a class="abs store store-b"><i></i>Available on Play Shelf</a>
  </section>

  <section class="section team">
    <h2 class="abs h2" style="top:52px">Meet The Team</h2>
    <p class="abs team-sub">Meet the people behind app</p>
    <article class="abs member" style="left:143px">
      <div class="member-photo" role="img" aria-label="Portrait of the CEO" style="background:linear-gradient(180deg,#c9cdd1,#7b6f66 70%,#3a3a3c)"></div>
      <div class="member-name">Walter M. Ruano<small>CEO</small></div>
      <div class="socials"><i></i><i></i><i></i></div>
    </article>
    <article class="abs member" style="left:297px">
      <div class="member-photo" role="img" aria-label="Portrait of the designer" style="background:linear-gradient(180deg,#bdb5ac,#7a5a48 60%,#4a3a32)"></div>
      <div class="member-name">Ann T. Kessler<small>Designer</small></div>
      <div class="socials"><i></i><i></i><i></i></div>
    </article>
    <article class="abs member" style="left:450px">
      <div class="member-photo" role="img" aria-label="Portrait of the project manager" style="background:linear-gradient(180deg,#4a3322,#2a1e17 60%,#1b1b1e)"></div>
      <div class="member-name">David M. Brookes<small>Project Manager</small></div>
      <div class="socials"><i></i><i></i><i></i></div>
    </article>
  </section>

  <section class="section contact">
    <h2 class="abs h2" style="top:52px">Contact Us</h2>
    <p class="abs contact-sub">Please, fill out the contact form below.</p>
    <div class="abs input" style="top:123px;height:20px;padding-top:6px">Name *</div>
    <div class="abs input" style="top:153px;height:20px;padding-top:6px">Email *</div>
    <div class="abs input" style="top:184px;height:65px">Message *</div>
    <button class="abs btn-red send">Send</button>
  </section>

  <footer class="section footer">
    <div class="abs f-brand"><i class="dot"></i><span>StageLoop</span></div>
    <p class="abs f-about">Lorem ipsum dolor sit amet, consectetuer adipiscing elit. Aenean commodo ligula eget dolor. Aenean massa. Cum sociis natoque penatibus.</p>
    <div class="abs f-col" style="left:197px"><h4>Quick Links</h4><ul><li>Domain</li><li>Hosting</li><li>Billing</li><li>Blog</li><li>Contact</li></ul></div>
    <div class="abs f-col" style="left:314px"><h4>Support</h4><ul><li>Product Support</li><li>Community</li><li>Report Abuse</li></ul></div>
    <div class="abs f-col" style="left:447px"><h4>Account</h4><ul><li>My Account</li><li>My Renewals</li><li>Create Account</li></ul></div>
    <div class="abs f-col f-news" style="left:578px"><h4>News Letter Sign-Up</h4></div>
    <div class="abs news"><span>Email Address</span><b>Submit</b></div>
    <div class="abs f-rule"></div>
    <p class="abs f-copy">© 2019 StageLoop.inc</p>
    <p class="abs f-legal"><span>Privacy Policy</span><span>Terms &amp; Conditions</span></p>
  </footer>
</main>
</body>
</html>
```